Creative - Appealing - Business Card Design Project

Looking for a Business card design (vector artwork) for an existing company called 'Fernway Sound'. We operate in the entertainment industry specializing in audio system design and rental, however; we also deal with other sectors of the entertainment industry including lighting, video, staging and power system design and rental. We would like to see designs that don't focus too much on audio but include elements encompassing everything else.

Double sided business card, following our new colour scheme and logo, which is attached. The card would ideally be creative and eye catching to draw in new customers in the elegant event production market, such as weddings & corporate affairs.

Target Market(s)

High end corporate clients, wedding clients

Industry/Entity Type

Entertainment

Requirements
Must have
• Our contact details, these can be worded & listed however you think appropriate as part as the design

Business Name - Fernway Sound
My Name - Dominic Harwell
Web Address - www.fernwaysound-example.com
Mobile Number - 07914 362 517
Office Number - 0330 481 7265
Email - dom@fernwaysound-example.com

The name, email and mobile number would need to be able to be changed to my business partners also.

The font used on our logo is Sansation
Nice to have
• On one side maybe a word cloud involving the services in which we can provide; Lighting, Sound, Event Production, Staging, LED Uplighting, Projection Mapping, Wedding Hire

On the other side, all the important credentials of contact.
Should not have
• The design should not use any old style fonts (i.e Times New Roman, Gothic etc) or on the other side of the scale, any 'jokey' fonts (i.e. Comic Sans).

The font to be used is Sansation

```html
<!DOCTYPE html>
<html lang="en">
<head>
<meta charset="utf-8">
<title>Fernway Sound – Business Card</title>
<link rel="stylesheet" href="https://fonts.googleapis.com/css2?family=Sansation:ital,wght@0,400;0,700;1,400&display=swap">
<style>
  :root {
    --backdrop: #ece6dc;
    --purple-top: #5f4190;
    --purple-bottom: #33265a;
    --brand-purple: #4e3486;
    --lavender: #ddd2f2;
    --service-text: #a898d0;
    --card-white: #ffffff;
    --ink-grey: #666666;
  }
  html, body {
    margin: 0;
    padding: 0;
    width: 1200px;
    height: 800px;
    overflow: hidden;
    background: var(--backdrop);
    font-family: "Sansation", "Exo 2", sans-serif;
  }
  .canvas {
    position: relative;
    width: 1200px;
    height: 800px;
  }
  .card {
    position: absolute;
    width: 296px;
    height: 483px;
    border-radius: 20px;
    box-sizing: border-box;
  }
  .card-front {
    left: 275px;
    top: 88px;
    background: linear-gradient(165deg, var(--purple-top) 0%, var(--purple-bottom) 100%);
  }
  .brand-name {
    position: absolute;
    left: 0;
    top: 104px;
    width: 174px;
    text-align: center;
    margin: 0;
    color: var(--lavender);
    font-weight: 700;
    font-size: 22px;
    line-height: 25px;
    letter-spacing: 0.5px;
    text-transform: uppercase;
  }
  .services {
    position: absolute;
    right: 26px;
    top: 352px;
    margin: 0;
    padding: 0;
    list-style: none;
    text-align: right;
  }
  .services li {
    color: var(--service-text);
    font-style: italic;
    font-size: 13px;
    line-height: 23px;
  }
  .card-back {
    left: 612px;
    top: 204px;
    background: var(--card-white);
    text-align: center;
    color: var(--ink-grey);
  }
  .back-brand {
    position: absolute;
    left: 0;
    right: 0;
    top: 84px;
    margin: 0;
    color: var(--brand-purple);
    font-weight: 700;
    font-size: 17px;
    letter-spacing: 0.5px;
    text-transform: uppercase;
  }
  .holder-name {
    position: absolute;
    left: 0;
    right: 0;
    top: 168px;
    margin: 0;
    font-weight: 700;
    font-size: 14.5px;
    letter-spacing: 0.6px;
    text-transform: uppercase;
    color: var(--ink-grey);
  }
  .contact-list {
    position: absolute;
    left: 0;
    right: 0;
    top: 216px;
    margin: 0;
    padding: 0;
    list-style: none;
    font-size: 12.5px;
  }
  .contact-list li { line-height: 25px; }
  .contact-list .web { margin-top: 6px; }
  .web .domain { color: var(--brand-purple); }
  .address {
    position: absolute;
    left: 0;
    right: 0;
    top: 379px;
    margin: 0;
    font-style: normal;
    font-size: 12.5px;
    line-height: 25px;
  }
</style>
</head>
<body>
<main class="canvas">
  <section class="card card-front" aria-label="Card front">
    <h1 class="brand-name">Fernway<br>Sound</h1>
    <ul class="services">
      <li>Event Production</li>
      <li>Staging</li>
      <li>Wedding Hire</li>
      <li>LED Uplighting</li>
      <li>Projection Mapping</li>
    </ul>
  </section>

  <section class="card card-back" aria-label="Card back">
    <p class="back-brand">Fernway Sound</p>
    <h2 class="holder-name">Dominic Harwell</h2>
    <ul class="contact-list">
      <li>07914 362 517</li>
      <li>0330 481 7265</li>
      <li>dom@fernwaysound-example.com</li>
      <li class="web">www.<span class="domain">fernwaysound-example</span>.com</li>
    </ul>
    <address class="address">
      48 Harrow Lane<br>
      Kestrel Park<br>
      Ashbourne City Northshire
    </address>
  </section>
</main>
</body>
</html>
```